Stubby holder (a beer holder... see examples in files) design. I need a stubby holder design that has our logo with the black background.
I need it obvious that "Plovix" refers to alcohol breathalysers... which is our business.
Feel free to use your imagination for design.

Target Market(s)

Drivers, beer, wine, spirits.

Industry/Entity Type

Alcohol breathalysers

Requirements
Must have
• Logo, and "Fuel Cell Technology"

```html
<!DOCTYPE html>
<html lang="en">
<head>
<meta charset="utf-8">
<title>Plovix stubby holder wrap</title>
<link rel="stylesheet" href="https://fonts.googleapis.com/css2?family=Archivo:wdth,wght@125,900&family=Montserrat:wght@700&family=Questrial&display=swap">
<style>
  :root {
    --stage: #141414;
    --panel: #050505;
    --panel-glow: #1e1e1e;
    --band-red: #ff0000;
    --accent-red: #ee3a3c;
    --device-red: #d8282c;
    --bubble-shade: #2a0a0b;
    --ink-white: #ffffff;
    --ink-dark: #111111;
  }
  html, body {
    margin: 0;
    padding: 0;
    width: 800px;
    height: 1200px;
    overflow: hidden;
    background: var(--stage);
  }
  .canvas {
    position: relative;
    width: 800px;
    height: 1200px;
    display: flex;
    align-items: center;
    justify-content: center;
  }
  .wrap-artwork {
    width: 720px;
    height: 306px;
    display: block;
  }
  .tagline {
    font-family: "Montserrat", Arial, sans-serif;
    font-weight: 700;
    font-size: 13px;
    fill: var(--ink-dark);
    letter-spacing: 0.2px;
  }
  .brand-name {
    font-family: "Archivo", "Arial Black", sans-serif;
    font-weight: 900;
    font-stretch: 125%;
    font-variation-settings: "wdth" 125;
    font-size: 80px;
    fill: var(--ink-white);
    letter-spacing: 2px;
  }
  .web-address {
    font-family: "Questrial", Arial, sans-serif;
    font-size: 31px;
    fill: var(--ink-white);
  }
</style>
</head>
<body>
<main class="canvas">
  <svg class="wrap-artwork" viewBox="0 0 873 371" xmlns="http://www.w3.org/2000/svg" aria-label="Plovix stubby holder wrap artwork">
    <defs>
      <radialGradient id="panel-glow" cx="50%" cy="45%" r="60%">
        <stop offset="0%" stop-color="var(--panel-glow)"/>
        <stop offset="100%" stop-color="var(--panel)"/>
      </radialGradient>
      <clipPath id="panel-clip">
        <rect x="0" y="30" width="873" height="308"/>
      </clipPath>
    </defs>

    <rect class="band-top" x="0" y="0" width="873" height="21" fill="var(--band-red)"/>
    <rect class="band-bottom" x="0" y="352" width="873" height="19" fill="var(--band-red)"/>

    <g class="main-panel" clip-path="url(#panel-clip)">
      <rect x="0" y="30" width="873" height="308" fill="var(--panel)"/>
      <rect role="img" aria-label="Faint molecular pattern background" x="160" y="30" width="560" height="308" fill="url(#panel-glow)"/>

      <path class="corner-left" d="M0,30 H350 C220,40 70,120 0,285 Z" fill="var(--accent-red)"/>
      <path class="swoosh-line" d="M0,300 C70,140 210,50 350,32" fill="none" stroke="var(--panel)" stroke-width="5"/>
      <path class="swoosh-line" d="M0,312 C80,150 220,52 380,30" fill="none" stroke="var(--accent-red)" stroke-width="3"/>

      <path class="corner-right" d="M873,338 H490 C660,320 800,220 873,40 Z" fill="var(--accent-red)"/>
      <path class="swoosh-line" d="M873,28 C810,210 680,320 480,336" fill="none" stroke="var(--panel)" stroke-width="5"/>
      <path class="swoosh-line" d="M873,18 C800,210 660,326 470,338" fill="none" stroke="var(--accent-red)" stroke-width="3"/>

      <rect role="img" aria-label="Breathalyser device with mouthpiece" x="0" y="96" width="120" height="150" rx="8" fill="var(--device-red)"/>
      <rect role="img" aria-label="Breathalyser device with mouthpiece" x="738" y="106" width="128" height="164" rx="8" fill="var(--device-red)"/>
      <rect role="img" aria-label="Rising bubbles" x="128" y="236" width="90" height="102" rx="6" fill="var(--bubble-shade)"/>
      <rect role="img" aria-label="Rising bubbles" x="640" y="30" width="100" height="100" rx="6" fill="var(--bubble-shade)"/>

      <text class="tagline" x="8" y="46">ALCOHOL BREATHALYSERS</text>
      <text class="tagline" x="864" y="330" text-anchor="end">ALCOHOL BREATHALYSERS</text>
    </g>

    <text class="brand-name" x="436" y="195" text-anchor="middle">PLOVIX</text>
    <line class="rule" x1="182" y1="218" x2="418" y2="218" stroke="var(--ink-white)" stroke-width="3"/>
    <text class="web-address" x="690" y="229" text-anchor="end">plovix.com.au</text>
  </svg>
</main>
</body>
</html>
```